Business card design needed

It's a new business in town.Something so the name stands out.I need a logo for the B.R.K
I may all so use the design as a sign on a building

Contact Information for Business Card

B.R.K
Brackenvale Auto Detailing
42 Tillbury Crs
Brackenvale Vic 3819
Ph:(03)58264027
Mob:0417392658

```html
<!DOCTYPE html>
<html lang="en">
<head>
<meta charset="utf-8">
<title>Brackenvale Auto Detailing – Business Card</title>
<link rel="stylesheet" href="https://fonts.googleapis.com/css2?family=Rye&family=Questrial&display=swap">
<style>
  :root {
    --card-bg: #030303;
    --card-edge: #1a1a1a;
    --brand-blue: #1b7fd0;
    --chrome-light: #f4f4f4;
    --chrome-mid: #a9a9a9;
    --chrome-dark: #3a3a3a;
    --contact-grey: #8ea3b2;
  }
  html, body {
    margin: 0;
    padding: 0;
    width: 1200px;
    height: 693px;
    overflow: hidden;
    background: var(--card-bg);
  }
  .business-card {
    position: relative;
    width: 1200px;
    height: 693px;
    background: radial-gradient(ellipse at 50% 40%, #0c0c0c 0%, var(--card-bg) 70%);
    box-shadow: inset 0 0 0 2px var(--card-edge);
    box-sizing: border-box;
    overflow: hidden;
  }
  .brand-mark {
    position: absolute;
    left: 0;
    right: 0;
    top: 92px;
    margin: 0;
    text-align: center;
    font-family: "Rye", serif;
    font-weight: 400;
    font-size: 124px;
    line-height: 1;
    letter-spacing: 6px;
    color: var(--brand-blue);
  }
  .business-name {
    position: absolute;
    left: 0;
    right: 0;
    top: 384px;
    margin: 0;
    text-align: center;
    font-family: "Rye", serif;
    font-weight: 400;
    font-size: 60px;
    line-height: 1.1;
    font-variant: small-caps;
    letter-spacing: 1px;
    background: linear-gradient(180deg,
      var(--chrome-light) 0%,
      var(--chrome-mid) 45%,
      var(--chrome-dark) 55%,
      var(--chrome-light) 100%);
    -webkit-background-clip: text;
    background-clip: text;
    color: transparent;
  }
  .contact {
    position: absolute;
    margin: 0;
    font-family: "Questrial", sans-serif;
    font-style: normal;
    font-size: 32px;
    line-height: 37px;
    letter-spacing: 1px;
    color: var(--contact-grey);
  }
  .contact-address { left: 178px; top: 512px; }
  .contact-phones { left: 724px; top: 533px; }
  .contact span { display: block; }
</style>
</head>
<body>
  <main class="business-card">
    <p class="brand-mark">B.R.K</p>
    <h1 class="business-name">Brackenvale Auto Detailing</h1>
    <address class="contact contact-address">
      <span>42 Tillbury Crs</span>
      <span>Brackenvale</span>
      <span>Vic 3819</span>
    </address>
    <p class="contact contact-phones">
      <span>Ph: (03) 5826 4027</span>
      <span>Mob: 0417 392 658</span>
    </p>
  </main>
</body>
</html>
```